Gone before dawn

Creation of a cover for a detective story
Size: 14 x 20.5 cm
Title: Gone Before Dawn
Author: Bastien Mardelot
Publisher (at the bottom of the page): Editions Sorbel
Abstract: A surgeon in a hospital is faced with a series of post-operative infections. He suspects foul play due to the ongoing hostility of one of his colleagues.
Suggested Visual Elements:
- Hospital
- Operative room, with a surgeon and an African anesthetic
- Beautiful woman of 40 years old.
Updates
Target Market(s)
Adults
Industry/Entity Type
Book
Look and feel
Each slider illustrates characteristics of the customer's brand and the style your logo design should communicate.

```html
<!DOCTYPE html>
<html lang="en">
<head>
<meta charset="utf-8">
<title>Gone Before Dawn — Cover Wrap</title>
<link rel="stylesheet" href="https://fonts.googleapis.com/css2?family=Courier+Prime:wght@400;700&family=Montserrat:wght@400;500;600&display=swap">
<style>
  :root {
    --page-bg: #ffffff;
    --back-black: #000000;
    --spine-navy: #0e1322;
    --ink-white: #ffffff;
    --ink-black: #050505;
    --photo-deep: #0d1430;
    --photo-mid: #3a4a78;
    --photo-glow: #f4e9ef;
    --photo-warm: #c9a98c;
  }
  html, body {
    margin: 0;
    padding: 0;
    width: 1200px;
    height: 1200px;
    overflow: hidden;
    background: var(--page-bg);
  }
  .cover-wrap {
    position: absolute;
    left: 40px;
    top: 198px;
    width: 1120px;
    height: 804px;
    display: flex;
  }
  .back-cover {
    position: relative;
    width: 537px;
    height: 100%;
    background: var(--back-black);
    color: var(--ink-white);
  }
  .back-title {
    position: absolute;
    top: 112px;
    left: 0;
    width: 100%;
    margin: 0;
    text-align: center;
    font-family: "Courier Prime", "Courier New", monospace;
    font-weight: 400;
    font-size: 34px;
    letter-spacing: 0.02em;
    word-spacing: -0.25em;
    line-height: 1;
  }
  .back-blurb {
    position: absolute;
    top: 164px;
    left: 68px;
    width: 402px;
    font-family: "Montserrat", Arial, sans-serif;
    font-size: 12.6px;
    line-height: 20.1px;
    text-align: justify;
  }
  .back-blurb p { margin: 0 0 20.1px; }
  .spine {
    width: 48px;
    height: 100%;
    background: var(--spine-navy);
  }
  .spine svg, .front-cover svg { display: block; width: 100%; height: 100%; }
  .front-cover {
    position: relative;
    width: 535px;
    height: 100%;
  }
  .serif-type { font-family: "Courier Prime", "Courier New", monospace; }
  .sans-type { font-family: "Montserrat", Arial, sans-serif; }
</style>
</head>
<body>
  <main class="cover-wrap">
    <section class="back-cover">
      <h2 class="back-title">GONE BEFORE DAWN</h2>
      <div class="back-blurb">
        <p>Lorem ipsum dolor sit amet, consectetur adipiscing elit, sed do eiusmod tempor incididunt ut labore et dolore magna aliqua. Quis ipsum suspendisse ultrices gravida. Risus commodo viverra maecenas accumsan lacus vel facilisis. Lorem ipsum dolor sit amet, consectetur adipiscing elit, sed do eiusmod tempor incididunt ut labore et dolore magna aliqua. Quis ipsum suspendisse ultrices gravida. Risus commodo viverra maecenas accumsan lacus vel facilisis. Lorem ipsum dolor sit amet, consectetur adipiscing elit, sed do eiusmod tempor incididunt ut labore et dolore magna aliqua. Quis ipsum suspendisse ultrices gravida. Risus commodo viverra maecenas accumsan lacus vel facilisis. Lorem ipsum dolor sit amet, consectetur adipiscing elit, sed do eiusmod tempor incididunt ut labore et dolore magna aliqua. Quis ipsum suspendisse ultrices gravida. Risus commodo viverra maecenas accumsan lacus vel facilisis.</p>
        <p>Lorem ipsum dolor sit amet, consectetur adipiscing elit, sed do eiusmod tempor incididunt ut labore et dolore magna aliqua. Quis ipsum suspendisse ultrices gravida. Risus commodo viverra maecenas accumsan lacus vel facilisis. Lorem ipsum dolor sit amet, consectetur adipiscing elit, sed do eiusmod tempor incididunt ut labore et dolore magna aliqua. Quis ipsum suspendisse ultrices gravida. Risus commodo viverra maecenas accumsan lacus vel facilisis.</p>
      </div>
    </section>

    <section class="spine">
      <svg viewBox="0 0 48 883" preserveAspectRatio="none">
        <g fill="var(--ink-white)">
          <text class="serif-type" transform="translate(14 50) rotate(90)" font-size="34" font-weight="400" textLength="380" lengthAdjust="spacingAndGlyphs">GONE BEFORE DAWN</text>
          <text class="serif-type" transform="translate(17 470) rotate(90)" font-size="21" font-weight="400" textLength="262" lengthAdjust="spacingAndGlyphs">BASTIEN MARDELOT</text>
          <text class="sans-type" transform="translate(20 775) rotate(90)" font-size="9.5" font-weight="600" textLength="98" lengthAdjust="spacingAndGlyphs">EDITIONS SORBEL</text>
        </g>
      </svg>
    </section>

    <section class="front-cover">
      <svg viewBox="0 0 588 883" preserveAspectRatio="none">
        <defs>
          <radialGradient id="corridorLight" cx="0.6" cy="0.52" r="0.7">
            <stop offset="0" stop-color="var(--photo-glow)"/>
            <stop offset="0.18" stop-color="var(--photo-warm)"/>
            <stop offset="0.45" stop-color="var(--photo-mid)"/>
            <stop offset="1" stop-color="var(--photo-deep)"/>
          </radialGradient>
        </defs>
        <rect class="cover-photo" x="0" y="0" width="588" height="883" fill="url(#corridorLight)" role="img" aria-label="Photograph of a dim hospital corridor with a silhouetted man carrying a case, lit from the far end"/>
        <g class="serif-type" font-weight="700" text-anchor="middle">
          <text x="293" y="225" font-size="200" fill="var(--ink-white)" textLength="430" lengthAdjust="spacingAndGlyphs">GONE</text>
          <text x="300" y="440" font-size="175" fill="var(--ink-black)" textLength="470" lengthAdjust="spacingAndGlyphs">BEFORE</text>
          <text x="293" y="758" font-size="290" fill="var(--ink-white)" textLength="470" lengthAdjust="spacingAndGlyphs">DAWN</text>
        </g>
        <text class="serif-type" x="296" y="805" font-size="22" font-weight="700" fill="var(--ink-white)" text-anchor="middle" letter-spacing="2">BASTIEN MARDELOT</text>
        <text class="sans-type" x="296" y="836" font-size="11" font-weight="600" fill="var(--ink-white)" text-anchor="middle" letter-spacing="1">EDITIONS SORBEL</text>
      </svg>
    </section>
  </main>
</body>
</html>
```